Maren Tolliver Luxury Wellness Profile Booklet

I am a luxury wellness property agent and would like to create my personal profile booklet. I want this to feel luxurious, minimalist, informative and the philosophy behind wellness and property the cPAGE 1 — THE COVER

Very minimal.

MAREN TOLLIVER

LUXURY WELLNESS PROPERTY

PROPERTY • WELLNESS • LIFESTYLE

Keel Ashby Coastline Group

Large photograph of you — preferably walking through a beautiful waterfront property or standing naturally within an architectural setting.

At the bottom:

Hope Island • Sanctuary Cove • Helensvale

Small Keel Ashby logo.

PAGE 2 — THE OPENING STATEMENT

A beautiful full-page lifestyle photograph.

Overlaid:

WHERE PROPERTY
MEETS WELLBEING

“A home is more than an address. It is the environment in which life unfolds.”

Then a short introduction:

Opening Profile

I believe the most exceptional properties are not defined simply by their architecture, address or price.

They are defined by how they make you feel.

Natural light. Water views. Privacy. Green space. Indoor-outdoor living. A place to unwind, entertain, recharge and reconnect.

My approach to luxury property brings these elements together — combining strategic real estate expertise with a genuine understanding of wellness, lifestyle and the way people want to live today.

Because when we understand the lifestyle behind the property, we can create a more compelling story around it.

PAGE 3 — MEET MAREN

Large portrait of you on one side.

Other side:

MEET MAREN

20+ YEARS OF PROPERTY EXPERIENCE

Commercial
Residential
Project Sales
Luxury & Lifestyle Property

Then:

About Maren

With more than 20 years' experience across commercial, residential and project sales, I have built my career around relationships, strategic marketing and delivering exceptional outcomes for my clients.

My approach is warm, considered and highly personal.

I believe sellers deserve more than a listing campaign. They deserve a clear strategy, honest communication and an agent who understands what makes their property valuable — both financially and emotionally.

Today, my focus is luxury lifestyle property across the Northern Gold Coast, with a particular passion for Hope Island, Sanctuary Cove and selected waterfront gated estates in Helensvale.

PAGE 4 — WHY WELLNESS?

This is where your differentiation becomes really powerful.

Full-bleed photograph of:

pool
outdoor entertaining
greenery
water
spa
wellness room
person walking beside water
WELLNESS IS THE NEW LUXURY

Then:

Wellness Philosophy

Luxury has evolved.

Today, luxury is not only about beautiful finishes, expansive living spaces or an impressive address.

It is privacy.

It is waking to water.

It is natural light flooding through the home.

It is having space to breathe.

It is stepping outside into nature, walking along the water, enjoying a morning swim, entertaining beside the pool or creating a private sanctuary at home.

These lifestyle elements increasingly shape the way buyers experience and value a property.

This is where my passion for wellness becomes part of my property approach.

PAGE 5 — MY WELLNESS JOURNEY

This page makes the wellness positioning credible rather than simply being a marketing slogan.

MY WELLNESS JOURNEY

You could use 3 small photographs:

BLOOMFOLD TOTS
QUILLON WELLNESS CENTRE
LUXURY WELLNESS PROPERTY

Copy:

Wellness Journey

My connection with wellness began outside of real estate.

After stepping away from property, I founded Bloomfold Tots, developing an organic children's nutritional product with a focus on natural ingredients and wellbeing.

I later launched Quillon Wellness Centre, further deepening my understanding of wellness, health-conscious lifestyles and the importance of creating environments that support how we live.

Today, I bring that perspective back into property.

I see homes differently — not simply as buildings, but as environments for living, restoring, entertaining and thriving.

PAGE 6 — THE MAREN TOLLIVER DIFFERENCE

This should be one of your strongest pages.

A DIFFERENT WAY OF SEEING PROPERTY

Use six elegant icons or small images:

01 — LIFESTYLE

I look beyond the floor plan to understand how buyers will actually experience the home.

02 — WELLNESS

I identify the spaces and features that contribute to wellbeing and lifestyle.

03 — PRESENTATION

I create a campaign that makes the property feel aspirational, memorable and emotionally engaging.

04 — STORY

Every exceptional property has a story. I find it, refine it and communicate it.

05 — STRATEGY

From positioning and buyer targeting to campaign execution and negotiation, every element has a purpose.

06 — RELATIONSHIPS

Trust, transparency and communication remain at the centre of every campaign.

PAGE 7 — YOUR PROPERTY STORY

This could be a beautiful editorial spread.

EVERY HOME HAS A STORY

Then:

My role is to discover what makes yours extraordinary.

Three questions:

WHAT MAKES YOUR PROPERTY DIFFERENT?

Architecture?
Waterfront?
Views?
Privacy?
Garden?
Location?

HOW DOES IT MAKE PEOPLE FEEL?

Calm?
Inspired?
Connected?
Entertained?
Relaxed?

WHO WILL FALL IN LOVE WITH IT?

Families?
Executives?
Downsizers?
Boaties?
Golfers?
Wellness-focused buyers?
Lifestyle purchasers?

Then:

I turn these answers into your property's story.

PAGE 8 — YOUR NORTHERN GOLD COAST

Beautiful aerial/waterfront image.

MY MARKET

HOPE ISLAND

SANCTUARY COVE

HELENSVALE

WATERFRONT & GATED ESTATES

Copy:

Northern Gold Coast

I specialise in the lifestyle-driven property market of the Northern Gold Coast.

From the waterfront homes and private enclaves of Hope Island and Sanctuary Cove to the established gated estates of Helensvale, I understand the lifestyle characteristics that attract buyers to this part of the Gold Coast.

Having personally experienced the lifestyle of these communities, I understand that buyers are often purchasing far more than a house.

They are buying a way of life.

PAGE 9 — THE WELLNESS PROPERTY

This could become your signature page.

WHAT MAKES A WELLNESS HOME?

Use a sophisticated grid:

WATER
Pools • Waterfront • Marina • Water views

NATURE
Green space • Gardens • Reserve outlooks • Walking trails

LIGHT
Natural light • Orientation • Open spaces

MOVEMENT
Walking • Golf • Boating • Outdoor living

RESTORATION
Spa • Sauna • Cold plunge • Retreat spaces

CONNECTION
Entertaining • Family • Indoor/outdoor living

Bottom:

The most desirable luxury is often the way a home makes you feel.

PAGE 10 — THE SELLING EXPERIENCE
YOUR HOME. YOUR STORY. YOUR CAMPAIGN.

I would make this a simple six-stage journey:

01 — DISCOVER
Understand your property, your goals and your lifestyle.

↓

02 — POSITION
Establish the property's unique market position.

↓

03 — PREPARE
Presentation, styling and strategic recommendations.

↓

04 — CREATE
Photography, film, editorial storytelling and digital marketing.

↓

05 — CONNECT
Targeted buyer engagement and database activation.

↓

06 — NEGOTIATE
Strategic negotiation designed to maximise the opportunity.

PAGE 11 — THE POWER OF PRESENTATION

Large before/after style photography.

FIRST IMPRESSIONS ARE EVERYTHING

Copy:

We don't get a second opportunity to create a first impression.

Then explain your approach to:

styling
photography
cinematic video
twilight imagery
aerial photography
lifestyle storytelling
digital advertising
targeted database marketing
buyer follow-up
auction strategy

Importantly, don't make this page feel like a generic list of marketing products.

Frame everything around:

Creating desire before creating urgency.
PAGE 12 — PROVEN RESULTS

Now introduce your actual results.

RESULTS THAT BUILD CONFIDENCE

Use your strongest results as elegant case studies.

For example:
4183 Pellingham Drive, Hope Island
$3,850,000
34 Days On The Market

$2.90M
52 Amberlyn Vale Boulevard, Helensvale
Sold within 45 days

Include your result and the property's story.

$2.15M

3/9 Amberlyn Vale Boulevard

Waterfront Villa

Then potentially:

28 DAYS

5218 Thistlewood Boulevard, Hope Island

Under contract following relaunch

If a result subsequently changed because the contract fell through, be careful about how you describe the current status. We can make this page completely accurate to the final outcome.

PAGE 13 — THE KEEL ASHBY ADVANTAGE

This is where you let the brand support you, rather than letting the booklet become a Keel Ashby corporate brochure.

PERSONAL SERVICE.
NATIONAL REACH.

Then a short statement about your Keel Ashby platform.

You could include:

POWERFUL BUYER DATABASE

LUXURY PROPERTY MARKETING

AUCTION EXPERTISE

DIGITAL REACH

LOCAL KNOWLEDGE

NATIONAL NETWORK

And a short line:

The personal attention of a specialist agent, supported by the strength of a globally recognised property network.

PAGE 14 — WHAT YOU CAN EXPECT FROM ME

This page is very important for your seller proposition.

MY PROMISE TO YOU

TRANSPARENCY

Clear advice, honest feedback and no unnecessary promises.

COMMUNICATION

You will know what is happening throughout your campaign.

STRATEGY

Every decision is made with your property, market and objectives in mind.

ATTENTION TO DETAIL

Your home deserves meticulous preparation and presentation.

PERSONAL SERVICE

You deal directly with me throughout your campaign.

RESULT FOCUS

My role is to create the strongest possible environment for a successful sale.

PAGE 15 — THE CLOSING PAGE

This should be very luxurious and emotional.

Beautiful photograph of water at sunset / luxury pool / Hope Island lifestyle.

YOUR HOME.
YOUR NEXT CHAPTER.

Then:

Closing Statement

Selling a home is rarely just a transaction.

It is the closing of one chapter and the beginning of another.

My role is to make the journey feel considered, strategic and personal — while creating the strongest possible opportunity for your property in the marketplace.

Thank you for considering me to represent your home.

I would be honoured to tell its story.

Then your details:

MAREN TOLLIVER

Luxury Wellness Property

0471 536 802

BACK COVER

Keep it extremely clean.

Your photograph or perhaps a beautiful Gold Coast waterfront image.

MAREN TOLLIVER

LUXURY WELLNESS PROPERTY

0471 536 802

Keel Ashby logoollaboration. I can send a full brief if required.

Target Market(s)

Luxury Property Owners

Industry/Entity Type

Wellness Luxury Real Estate Lifestyle

Requirements
Must have
• A luxurious minimalist clean feel

```html
<!DOCTYPE html>
<html lang="en">
<head>
<meta charset="utf-8">
<title>Maren Tolliver – Luxury Wellness Profile Booklet</title>
<link href="https://fonts.googleapis.com/css2?family=Cormorant+Garamond:ital,wght@0,400;0,500;1,400&family=Montserrat:wght@400;500;600&family=Mrs+Saint+Delafield&display=swap" rel="stylesheet">
<style>
:root{
  --board:#a3a4a8;
  --cream:#f5f2ec;
  --paper:#fbfaf7;
  --ink:#1a1a1a;
  --night:#161718;
  --tile:#1f2422;
  --gold:#b89766;
  --teal:#5d8f8b;
  --grey:#6c6c6c;
  --light:#e9e6df;
}
*{margin:0;padding:0;box-sizing:border-box}
html,body{width:988px;height:1200px;overflow:hidden;background:var(--board)}
body{position:relative;font-family:"Montserrat",sans-serif;color:var(--ink)}
.spread-label{position:absolute;top:32px;font:400 7px "Montserrat",sans-serif;color:#f2f2f2;letter-spacing:.3px}
.page{position:absolute;width:188px;height:266px;overflow:hidden;background:var(--paper);box-shadow:0 2px 4px rgba(0,0,0,.25)}
.page *{position:absolute}
.page .flow,.page .flow *{position:static}
.photo{display:block}
.serif{font-family:"Cormorant Garamond",serif;font-weight:500;line-height:1.1;letter-spacing:.3px}
.italic{font-family:"Cormorant Garamond",serif;font-style:italic;line-height:1.25}
.small{font-size:2.6px;line-height:1.45;color:var(--grey)}
.label{font-size:2.3px;letter-spacing:.6px;text-transform:uppercase;font-weight:500}
.gold{color:var(--gold)}
.white{color:#fff}
.folio{right:10px;bottom:6px;font-size:2.2px;color:#999}
.brand-name{font-family:"Montserrat",sans-serif;font-size:4px;font-weight:600;letter-spacing:.4px;color:var(--ink);white-space:nowrap}
.rule{height:.6px;background:var(--gold)}
.card-dark{background:var(--tile)}
.num{font-family:"Cormorant Garamond",serif;color:var(--gold)}
</style>
</head>
<body>

<div class="spread-label" style="left:167px">BACK COVER</div>
<div class="spread-label" style="left:356px">FRONT COVER</div>

<!-- Back cover -->
<section class="page" style="left:97px;top:43px;background:#fff">
  <div class="photo" role="img" aria-label="Waterfront terrace with fire pit, palms and a moored yacht" style="left:0;top:0;width:188px;height:126px;background:linear-gradient(180deg,#9dbbd0 0%,#6f8a4e 40%,#4d6a3f 65%,#e6e1d6 100%)"></div>
  <div class="serif" style="top:137px;width:188px;text-align:center;font-size:10px">MAREN TOLLIVER</div>
  <div class="label" style="top:153px;width:188px;text-align:center">Luxury wellness property</div>
  <div class="label" style="top:165px;width:188px;text-align:center">Property &nbsp;|&nbsp; Wellness &nbsp;|&nbsp; Lifestyle</div>
  <div class="rule" style="top:181px;left:74px;width:40px"></div>
  <div style="top:193px;width:188px;text-align:center;font-size:3.6px">0471 536 802</div>
  <div style="top:206px;width:188px;text-align:center;font-size:2.3px">Hope Island • Sanctuary Cove • Helensvale</div>
  <div class="brand-name" style="top:230px;width:188px;text-align:center">Keel Ashby</div>
</section>

<!-- Front cover -->
<section class="page" style="left:288px;top:43px">
  <div class="photo" role="img" aria-label="Portrait of the agent walking down a bright staircase" style="inset:0;background:linear-gradient(100deg,#f6f1ea 0%,#efe6da 55%,#e3d3c3 75%,#d8c7b8 100%)"></div>
  <div class="label" style="top:17px;width:188px;text-align:center;font-size:3.4px;letter-spacing:1.6px">Luxury wellness property</div>
  <div style="top:30px;left:8px;font-family:'Mrs Saint Delafield',cursive;font-size:40px;line-height:.9;color:var(--ink)">Maren<br>&nbsp;&nbsp;Tolliver</div>
  <div class="italic" style="top:106px;left:8px;width:96px;font-size:4.4px">A considered approach to luxury property, built around lifestyle, wellbeing and the way people want to live.</div>
  <div style="top:200px;left:8px;font-size:2.6px">Hope Island &nbsp;• &nbsp;Sanctuary Cove &nbsp;• &nbsp;Helensvale</div>
  <div style="top:212px;left:8px;font-size:2.6px">Keel Ashby Coastline Group</div>
  <div class="brand-name" style="top:230px;left:8px">Keel Ashby</div>
</section>

<!-- Page 02 -->
<section class="page" style="left:512px;top:43px;background:var(--cream)">
  <div class="photo" role="img" aria-label="Monochrome kitchen with arched alcove and teal bar stools" style="left:0;top:0;width:188px;height:101px;background:linear-gradient(180deg,#f4f4f2 0%,#d9d9d6 55%,#2b2b2b 78%,#5b8e8a 92%,#2a2a2a 100%)"></div>
  <div style="left:0;top:101px;width:188px;height:27px;background:var(--night)"></div>
  <div class="serif white" style="left:13px;top:105px;font-size:9px">WHERE PROPERTY<br>MEETS WELLBEING</div>
  <div class="italic" style="left:13px;top:145px;width:162px;font-size:4.6px">“A home is more than an address. It is the environment in which life unfolds.”</div>
  <div class="small" style="left:13px;top:171px;width:76px;color:var(--ink)">I believe the most exceptional properties are not defined simply by their architecture, address or price.<br><br>They are defined by how they make you feel.<br><br>Natural light. Water views. Privacy. Green space. Indoor-outdoor living. A place to unwind, entertain, recharge and reconnect.</div>
  <div class="small" style="left:98px;top:171px;width:76px">My approach to luxury property brings these elements together — combining strategic real estate expertise with a genuine understanding of wellness, lifestyle and the way people want to live today.<br><br>Because when we understand the lifestyle behind the property, we can create a more compelling story around it.</div>
  <div class="folio">02</div>
</section>

<!-- Page 03 -->
<section class="page" style="left:703px;top:43px">
  <div class="photo" role="img" aria-label="Portrait of the agent seated in a soft neutral interior" style="left:90px;top:0;width:98px;height:266px;background:linear-gradient(90deg,#fbfaf7 0%,#f1ebe2 30%,#e7ddd0 100%)"></div>
  <div class="serif" style="left:13px;top:29px;font-size:9.5px">20+ YEARS<br>OF PROPERTY<br>EXPERIENCE</div>
  <div class="rule" style="left:13px;top:83px;width:27px"></div>
  <div class="label" style="left:13px;top:92px;width:64px;height:6px;background:var(--light);text-align:center;line-height:6px;font-size:1.8px">Commercial</div>
  <div class="label" style="left:13px;top:103px;width:64px;height:6px;background:var(--light);text-align:center;line-height:6px;font-size:1.8px">Residential</div>
  <div class="label" style="left:13px;top:114px;width:64px;height:6px;background:var(--light);text-align:center;line-height:6px;font-size:1.8px">Project sales</div>
  <div class="label white" style="left:13px;top:125px;width:64px;height:6px;background:var(--night);text-align:center;line-height:6px;font-size:1.8px">Luxury &amp; lifestyle property</div>
  <div class="label gold" style="left:13px;top:142px">About Maren</div>
  <div class="small" style="left:13px;top:150px;width:80px;font-size:2.3px">With more than 20 years’ experience across commercial, residential and project sales, I have built my career around relationships, strategic marketing and delivering exceptional outcomes for my clients.<br><br>My approach is warm, considered and highly personal. I believe sellers deserve more than a listing campaign. They deserve a clear strategy, honest communication and an agent who understands what makes their property valuable – both financially and emotionally.<br><br>Today, my focus is luxury lifestyle property across the Northern Gold Coast, with a particular passion for Hope Island, Sanctuary Cove and selected waterfront gated estates in Helensvale.</div>
  <div class="folio">03</div>
</section>

<!-- Page 04 -->
<section class="page" style="left:97px;top:321px">
  <div class="photo" role="img" aria-label="Infinity pool and riverside trees at sunset" style="inset:0;background:linear-gradient(180deg,#3b4245 0%,#6b5f45 22%,#3d4a3a 45%,#2f3b3d 70%,#3b5a63 100%)"></div>
  <div class="serif white" style="left:14px;top:31px;font-size:11px">WELLNESS<br>IS THE NEW<br>LUXURY</div>
  <div class="italic gold" style="left:14px;top:102px;font-size:5px">Luxury has evolved.</div>
  <div class="small white" style="left:14px;top:115px;width:72px;font-size:2.4px">Today, luxury is not only about beautiful finishes, expansive living spaces or an impressive address.<br><br>It is privacy.<br>It is waking to water.<br>It is natural light flooding through the home.<br>It is having space to breathe.</div>
  <div class="small white" style="left:97px;top:115px;width:76px;font-size:2.4px">It is stepping outside into nature, walking along the water, entertaining beside the pool or creating a private sanctuary at home.<br><br>These lifestyle elements increasingly shape the way buyers experience and value a property.<br><br>This is where my passion for wellness becomes part of my property approach.</div>
  <div class="folio" style="color:#ccc">04</div>
</section>

<!-- Page 05 -->
<section class="page" style="left:288px;top:321px;background:var(--cream)">
  <div class="serif" style="left:14px;top:27px;font-size:8.5px">A CAREER SHAPED BY<br>PROPERTY + WELLBEING</div>
  <div class="rule" style="left:14px;top:50px;width:14px"></div>
  <div class="small" style="left:14px;top:69px;width:160px">My connection with wellness began outside of real estate. That experience now shapes the way I see homes: not simply as buildings, but as environments for living, restoring, entertaining and thriving.</div>
  <div style="left:13px;top:98px;width:50px;height:106px;background:#fff;border-left:.8px solid var(--gold)"></div>
  <div class="photo" role="img" aria-label="Agent in a bright white interior" style="left:13px;top:98px;width:50px;height:55px;background:linear-gradient(180deg,#f3f0ea,#d9d3ca)"></div>
  <div class="num" style="left:17px;top:157px;font-size:5px">01</div>
  <div class="label" style="left:17px;top:169px;font-size:1.9px">Bloomfold Tots</div>
  <div class="small" style="left:17px;top:176px;width:42px;font-size:1.9px">Founded an organic children's nutritional product focused on natural ingredients and wellbeing.</div>

  <div style="left:69px;top:98px;width:50px;height:106px;background:#fff;border-left:.8px solid var(--teal)"></div>
  <div class="photo" role="img" aria-label="Agent relaxing in a calm lounge" style="left:69px;top:98px;width:50px;height:55px;background:linear-gradient(180deg,#efeae3,#cfc8bd)"></div>
  <div class="num" style="left:73px;top:157px;font-size:5px;color:var(--teal)">02</div>
  <div class="label" style="left:73px;top:169px;width:42px;font-size:1.9px">Quillon Wellness Centre</div>
  <div class="small" style="left:73px;top:176px;width:42px;font-size:1.9px">Deepened an understanding of health-conscious lifestyles and environments that support how we live.</div>

  <div style="left:125px;top:98px;width:50px;height:106px;background:#fff;border-left:.8px solid var(--gold)"></div>
  <div class="photo" role="img" aria-label="Dark kitchen with teal stools" style="left:125px;top:98px;width:50px;height:55px;background:linear-gradient(180deg,#eeeeec 0%,#2a2a2a 60%,#5b8e8a 85%,#2a2a2a 100%)"></div>
  <div class="num" style="left:129px;top:157px;font-size:5px">03</div>
  <div class="label" style="left:129px;top:169px;width:42px;font-size:1.9px">Luxury Wellness Property</div>
  <div class="small" style="left:129px;top:176px;width:42px;font-size:1.9px">Bringing the wellness perspective back into property – combining expertise, lifestyle and story.</div>
  <div class="folio">05</div>
</section>

<!-- Page 06 -->
<section class="page" style="left:512px;top:321px;background:var(--night)">
  <div class="serif white" style="left:13px;top:27px;font-size:8.5px">A DIFFERENT WAY<br>OF SEEING PROPERTY</div>
  <div class="card-dark" style="left:13px;top:71px;width:75px;height:40px"></div>
  <div class="card-dark" style="left:97px;top:71px;width:75px;height:40px"></div>
  <div class="card-dark" style="left:13px;top:121px;width:75px;height:40px"></div>
  <div class="card-dark" style="left:97px;top:121px;width:75px;height:40px"></div>
  <div class="card-dark" style="left:13px;top:170px;width:75px;height:40px"></div>
  <div class="card-dark" style="left:97px;top:170px;width:75px;height:40px"></div>
  <div class="num" style="left:17px;top:75px;font-size:6px">01</div><div class="label white" style="left:33px;top:78px;font-size:1.8px">Lifestyle</div><div class="small" style="left:33px;top:84px;width:50px;font-size:1.8px;color:#aaa">I look beyond the floor plan to understand how buyers will actually experience the home.</div>
  <div class="num" style="left:101px;top:75px;font-size:6px">02</div><div class="label white" style="left:117px;top:78px;font-size:1.8px">Wellness</div><div class="small" style="left:117px;top:84px;width:50px;font-size:1.8px;color:#aaa">I identify the spaces and features that contribute to wellbeing and lifestyle.</div>
  <div class="num" style="left:17px;top:125px;font-size:6px">03</div><div class="label white" style="left:33px;top:128px;font-size:1.8px">Presentation</div><div class="small" style="left:33px;top:134px;width:50px;font-size:1.8px;color:#aaa">I create a campaign that makes the property feel aspirational, memorable and emotionally engaging.</div>
  <div class="num" style="left:101px;top:125px;font-size:6px">04</div><div class="label white" style="left:117px;top:128px;font-size:1.8px">Story</div><div class="small" style="left:117px;top:134px;width:50px;font-size:1.8px;color:#aaa">Every exceptional property has a story. I find it, refine it and communicate it.</div>
  <div class="num" style="left:17px;top:174px;font-size:6px">05</div><div class="label white" style="left:33px;top:177px;font-size:1.8px">Strategy</div><div class="small" style="left:33px;top:183px;width:50px;font-size:1.8px;color:#aaa">From positioning and buyer targeting to campaign execution and negotiation, every element has a purpose.</div>
  <div class="num" style="left:101px;top:174px;font-size:6px">06</div><div class="label white" style="left:117px;top:177px;font-size:1.8px">Relationships</div><div class="small" style="left:117px;top:183px;width:50px;font-size:1.8px;color:#aaa">Trust, transparency and communication remain at the centre of every campaign.</div>
  <div class="italic gold" style="left:13px;top:235px;font-size:4.2px">Luxury property deserves more than a generic campaign.</div>
  <div class="folio" style="color:#777">06</div>
</section>

<!-- Page 07 -->
<section class="page" style="left:703px;top:321px">
  <div class="photo" role="img" aria-label="White modern home with stone feature wall and pool" style="left:0;top:0;width:188px;height:100px;background:linear-gradient(180deg,#8fb4d6 0%,#dfe6ea 35%,#f2f2f0 60%,#4aa3c3 85%,#3a8aa8 100%)"></div>
  <div style="left:10px;top:95px;width:153px;height:22px;background:var(--paper)"></div>
  <div class="serif" style="left:16px;top:100px;font-size:9px">EVERY HOME<br>HAS A STORY</div>
  <div class="italic" style="left:16px;top:128px;font-size:4.3px;color:var(--grey)">My role is to discover what makes yours extraordinary.</div>
  <div class="num" style="left:13px;top:148px;font-size:2px">01</div><div class="label" style="left:13px;top:154px;width:48px;font-size:2px;line-height:1.3">What makes your property different?</div>
  <div class="num" style="left:68px;top:148px;font-size:2px">02</div><div class="label" style="left:68px;top:154px;width:48px;font-size:2px;line-height:1.3">How does it make people feel?</div>
  <div class="num" style="left:124px;top:148px;font-size:2px">03</div><div class="label" style="left:124px;top:154px;width:48px;font-size:2px;line-height:1.3">Who will fall in love with it?</div>
  <div class="rule" style="left:13px;top:172px;width:24px"></div><div class="rule" style="left:68px;top:172px;width:24px"></div><div class="rule" style="left:124px;top:172px;width:24px"></div>
  <div class="small" style="left:13px;top:181px;width:48px;font-size:2px">Architecture • Waterfront • Views • Privacy • Garden • Location</div>
  <div class="small" style="left:68px;top:181px;width:48px;font-size:2px">Calm • Inspired • Connected • Entertained • Relaxed</div>
  <div class="small" style="left:124px;top:181px;width:48px;font-size:2px">Families • Executives • Downsizers • Boaties • Golfers • Wellness-focused buyers • Lifestyle purchasers</div>
  <div style="left:13px;top:222px;width:161px;height:21px;background:var(--night)"></div>
  <div class="italic white" style="left:13px;top:229px;width:161px;text-align:center;font-size:4.3px">I turn these answers into your property’s story.</div>
  <div class="folio">07</div>
</section>

<!-- Page 08 -->
<section class="page" style="left:97px;top:600px">
  <div class="photo" role="img" aria-label="Riverfront jetty with moored yachts and garden fire pit" style="left:93px;top:0;width:95px;height:266px;background:linear-gradient(180deg,#e9ebe6 0%,#5b6e45 30%,#7d8a8d 55%,#c8c4b8 75%,#56703f 100%)"></div>
  <div style="left:0;top:0;width:93px;height:266px;background:#26292a"></div>
  <div class="label" style="left:14px;top:19px;color:#aaa;font-size:1.9px">Your Northern Gold Coast</div>
  <div class="serif white" style="left:14px;top:31px;font-size:12px">MY<br>MARKET</div>
  <div class="label white" style="left:14px;top:77px;font-size:2px">Hope Island</div>
  <div style="left:14px;top:83px;width:34px;height:.4px;background:#555"></div>
  <div class="label white" style="left:14px;top:89px;font-size:2px">Sanctuary Cove</div>
  <div style="left:14px;top:95px;width:34px;height:.4px;background:#555"></div>
  <div class="label white" style="left:14px;top:101px;font-size:2px">Helensvale</div>
  <div style="left:14px;top:107px;width:34px;height:.4px;background:#555"></div>
  <div class="label" style="left:14px;top:113px;color:#999;font-size:1.7px">Waterfront &amp; gated estates</div>
  <div class="small white" style="left:14px;top:139px;width:70px;font-size:2.2px">I specialise in the lifestyle-driven property market of the Northern Gold Coast.<br><br>From the waterfront homes and private enclaves of Hope Island and Sanctuary Cove to the established gated estates of Helensvale, I understand the lifestyle characteristics that attract buyers to this part of the Gold Coast.<br><br>Having personally experienced the lifestyle of these communities, I understand that buyers are often purchasing far more than a house.<br><br>They are buying a way of life.</div>
  <div class="folio" style="color:#ddd">08</div>
</section>

<!-- Page 09 -->
<section class="page" style="left:288px;top:600px;background:var(--cream)">
  <div class="label" style="left:13px;top:17px;color:#999;font-size:1.8px">The wellness property</div>
  <div class="serif" style="left:13px;top:27px;font-size:8.5px">WHAT MAKES A<br>WELLNESS HOME?</div>
  <div class="photo" role="img" aria-label="Kitchen with arched alcove and teal stools" style="left:130px;top:12px;width:47px;height:48px;background:linear-gradient(180deg,#eeeeec 0%,#2a2a2a 55%,#5b8e8a 80%,#2a2a2a 100%)"></div>
  <div style="left:13px;top:73px;width:70px;height:38px;background:#fff;border-left:.8px solid var(--gold)"></div>
  <div style="left:97px;top:73px;width:70px;height:38px;background:#fff;border-left:.8px solid var(--gold)"></div>
  <div style="left:13px;top:121px;width:70px;height:38px;background:#fff;border-left:.8px solid var(--teal)"></div>
  <div style="left:97px;top:121px;width:70px;height:38px;background:#fff;border-left:.8px solid var(--teal)"></div>
  <div style="left:13px;top:169px;width:70px;height:38px;background:#fff;border-left:.8px solid var(--gold)"></div>
  <div style="left:97px;top:169px;width:70px;height:38px;background:#fff;border-left:.8px solid var(--gold)"></div>
  <div class="num" style="left:16px;top:76px;font-size:11px;line-height:.95;color:#ddd2c2">0<br>1</div><div class="label" style="left:28px;top:80px;font-size:1.9px">Water</div><div class="small" style="left:28px;top:86px;width:52px;font-size:1.8px">Pools • Waterfront • Marina • Water views</div>
  <div class="num" style="left:100px;top:76px;font-size:11px;line-height:.95;color:#ddd2c2">0<br>2</div><div class="label" style="left:112px;top:80px;font-size:1.9px">Nature</div><div class="small" style="left:112px;top:86px;width:52px;font-size:1.8px">Green space • Gardens • Reserve outlooks • Walking trails</div>
  <div class="num" style="left:16px;top:124px;font-size:11px;line-height:.95;color:#c9d8d6">0<br>3</div><div class="label" style="left:28px;top:128px;font-size:1.9px">Light</div><div class="small" style="left:28px;top:134px;width:52px;font-size:1.8px">Natural light • Orientation • Open spaces</div>
  <div class="num" style="left:100px;top:124px;font-size:11px;line-height:.95;color:#c9d8d6">0<br>4</div><div class="label" style="left:112px;top:128px;font-size:1.9px">Movement</div><div class="small" style="left:112px;top:134px;width:52px;font-size:1.8px">Walking • Golf • Boating • Outdoor living</div>
  <div class="num" style="left:16px;top:172px;font-size:11px;line-height:.95;color:#ddd2c2">0<br>5</div><div class="label" style="left:28px;top:176px;font-size:1.9px">Restoration</div><div class="small" style="left:28px;top:182px;width:52px;font-size:1.8px">Spa • Sauna • Cold plunge • Retreat spaces</div>
  <div class="num" style="left:100px;top:172px;font-size:11px;line-height:.95;color:#ddd2c2">0<br>6</div><div class="label" style="left:112px;top:176px;font-size:1.9px">Connection</div><div class="small" style="left:112px;top:182px;width:52px;font-size:1.8px">Entertaining • Family • Indoor/outdoor living</div>
  <div class="rule" style="left:13px;top:223px;width:30px"></div>
  <div class="italic" style="left:13px;top:231px;width:150px;font-size:4.5px">The most desirable luxury is often the way a home makes you feel.</div>
  <div class="folio">09</div>
</section>

<!-- Page 10 -->
<section class="page" style="left:512px;top:600px;background:var(--night)">
  <div class="label" style="left:13px;top:16px;color:#888;font-size:1.8px">The selling experience</div>
  <div class="serif white" style="left:13px;top:27px;font-size:8.5px">YOUR HOME.<br>YOUR STORY.<br>YOUR CAMPAIGN.</div>
  <svg style="left:17px;top:88px" width="2" height="130"><g stroke="#555" stroke-width=".5"><line x1="1" y1="0" x2="1" y2="10"/><line x1="1" y1="26" x2="1" y2="36"/><line x1="1" y1="53" x2="1" y2="63"/><line x1="1" y1="79" x2="1" y2="89"/><line x1="1" y1="106" x2="1" y2="116"/></g></svg>
  <div class="num" style="left:14px;top:81px;font-size:5px">01</div><div class="label white" style="left:35px;top:82px;font-size:1.9px">Discover</div><div class="small" style="left:71px;top:82px;font-size:1.9px;color:#aaa">Understand your property, your goals and your lifestyle.</div>
  <div class="num" style="left:14px;top:107px;font-size:5px">02</div><div class="label white" style="left:35px;top:108px;font-size:1.9px">Position</div><div class="small" style="left:71px;top:108px;font-size:1.9px;color:#aaa">Establish the property’s unique market position.</div>
  <div class="num" style="left:14px;top:134px;font-size:5px">03</div><div class="label white" style="left:35px;top:135px;font-size:1.9px">Prepare</div><div class="small" style="left:71px;top:135px;font-size:1.9px;color:#aaa">Presentation, styling and strategic recommendations.</div>
  <div class="num" style="left:14px;top:160px;font-size:5px">04</div><div class="label white" style="left:35px;top:161px;font-size:1.9px">Create</div><div class="small" style="left:71px;top:161px;font-size:1.9px;color:#aaa">Photography, film, editorial storytelling and digital marketing.</div>
  <div class="num" style="left:14px;top:187px;font-size:5px">05</div><div class="label white" style="left:35px;top:188px;font-size:1.9px">Connect</div><div class="small" style="left:71px;top:188px;font-size:1.9px;color:#aaa">Targeted buyer engagement and database activation.</div>
  <div class="num" style="left:14px;top:213px;font-size:5px">06</div><div class="label white" style="left:35px;top:214px;font-size:1.9px">Negotiate</div><div class="small" style="left:71px;top:214px;font-size:1.9px;color:#aaa">Strategic negotiation designed to maximise the opportunity.</div>
  <div class="folio" style="color:#777">10</div>
</section>

<!-- Page 11 -->
<section class="page" style="left:703px;top:600px">
  <div class="photo" role="img" aria-label="Styled kitchen with arched black alcove and teal stools" style="left:0;top:0;width:188px;height:150px;background:linear-gradient(180deg,#f5f5f3 0%,#dcdcd9 40%,#262626 62%,#5b8e8a 80%,#2a2a2a 100%)"></div>
  <div style="left:11px;top:118px;width:164px;height:34px;background:var(--night)"></div>
  <div class="serif white" style="left:18px;top:125px;font-size:8.5px">FIRST IMPRESSIONS<br>ARE EVERYTHING</div>
  <div class="label gold" style="left:13px;top:163px;font-size:1.8px">The power of presentation</div>
  <div class="small" style="left:13px;top:170px;width:162px;color:var(--ink);font-size:2.2px">We don’t get a second opportunity to create a first impression. My presentation approach is designed to create desire before creating urgency.</div>
  <div class="flow" style="position:absolute;left:13px;top:197px;width:162px;display:grid;grid-template-columns:1fr 1fr;row-gap:4.6px;font-size:1.7px;letter-spacing:.5px;text-transform:uppercase;color:var(--grey)">
    <span style="display:flex;align-items:center;gap:3px"><b style="display:block;width:3.5px;height:3.5px;background:var(--gold)"></b>Styling</span>
    <span style="display:flex;align-items:center;gap:3px"><b style="display:block;width:3.5px;height:3.5px;background:var(--teal)"></b>Photography</span>
    <span style="display:flex;align-items:center;gap:3px"><b style="display:block;width:3.5px;height:3.5px;background:var(--teal)"></b>Cinematic video</span>
    <span style="display:flex;align-items:center;gap:3px"><b style="display:block;width:3.5px;height:3.5px;background:var(--gold)"></b>Twilight imagery</span>
    <span style="display:flex;align-items:center;gap:3px"><b style="display:block;width:3.5px;height:3.5px;background:var(--teal)"></b>Aerial photography</span>
    <span style="display:flex;align-items:center;gap:3px"><b style="display:block;width:3.5px;height:3.5px;background:var(--gold)"></b>Lifestyle storytelling</span>
    <span style="display:flex;align-items:center;gap:3px"><b style="display:block;width:3.5px;height:3.5px;background:var(--gold)"></b>Digital advertising</span>
    <span style="display:flex;align-items:center;gap:3px"><b style="display:block;width:3.5px;height:3.5px;background:var(--teal)"></b>Targeted database</span>
    <span style="display:flex;align-items:center;gap:3px"><b style="display:block;width:3.5px;height:3.5px;background:var(--gold)"></b>Buyer follow-up</span>
    <span style="display:flex;align-items:center;gap:3px"><b style="display:block;width:3.5px;height:3.5px;background:var(--gold)"></b>Auction strategy</span>
  </div>
  <div class="folio">11</div>
</section>

<!-- Page 12 -->
<section class="page" style="left:97px;top:879px;background:var(--cream)">
  <div class="label" style="left:13px;top:16px;color:#999;font-size:1.8px">Proven results</div>
  <div class="serif" style="left:13px;top:27px;font-size:8.5px">RESULTS THAT<br>BUILD CONFIDENCE</div>

  <div style="left:13px;top:69px;width:160px;height:43px;background:#fff"></div>
  <div class="photo" role="img" aria-label="Riverfront garden terrace" style="left:13px;top:69px;width:54px;height:43px;background:linear-gradient(180deg,#9bbad0,#5e7a45 55%,#ddd8cd)"></div>
  <div class="serif gold" style="left:73px;top:73px;font-size:6px">$3.85M</div>
  <div class="label" style="left:110px;top:75px;width:58px;text-align:right;font-size:1.6px;color:#999">34 days on the market</div>
  <div class="serif" style="left:73px;top:83px;font-size:4.4px">4183 Pellingham Drive, Hope Island</div>
  <div class="small" style="left:73px;top:93px;width:90px;font-size:1.8px">A selected result highlighting strategic positioning, presentation and buyer engagement.</div>

  <div style="left:13px;top:125px;width:160px;height:43px;background:#fff"></div>
  <div class="photo" role="img" aria-label="White modern home with pool" style="left:13px;top:125px;width:54px;height:43px;background:linear-gradient(180deg,#9bbfdc,#f0f0ee 45%,#3d98bb)"></div>
  <div class="serif gold" style="left:73px;top:129px;font-size:6px">$2.90M</div>
  <div class="label" style="left:110px;top:131px;width:58px;text-align:right;font-size:1.6px;color:#999">Sold within 45 days</div>
  <div class="serif" style="left:73px;top:139px;font-size:4.4px">52 Amberlyn Vale Boulevard, Helensvale</div>
  <div class="small" style="left:73px;top:149px;width:90px;font-size:1.8px">A selected result highlighting strategic positioning, presentation and buyer engagement.</div>

  <div style="left:13px;top:181px;width:160px;height:43px;background:#fff"></div>
  <div class="photo" role="img" aria-label="Kitchen with teal stools" style="left:13px;top:181px;width:54px;height:43px;background:linear-gradient(180deg,#efefed,#2a2a2a 55%,#5b8e8a 80%,#2a2a2a)"></div>
  <div class="serif gold" style="left:73px;top:185px;font-size:6px">$2.15M</div>
  <div class="label" style="left:110px;top:187px;width:58px;text-align:right;font-size:1.6px;color:#999">Waterfront villa</div>
  <div class="serif" style="left:73px;top:195px;font-size:4.4px">3/9 Amberlyn Vale Boulevard</div>
  <div class="small" style="left:73px;top:205px;width:90px;font-size:1.8px">A selected result highlighting strategic positioning, presentation and buyer engagement.</div>
  <div class="folio">12</div>
</section>

<!-- Page 13 -->
<section class="page" style="left:288px;top:879px">
  <div style="left:0;top:0;width:3px;height:266px;background:var(--gold)"></div>
  <div class="label" style="left:15px;top:18px;color:#999;font-size:1.8px">The Keel Ashby advantage</div>
  <div class="serif" style="left:15px;top:28px;font-size:8.5px">PERSONAL SERVICE.<br>NATIONAL REACH.</div>
  <div class="italic" style="left:15px;top:67px;width:155px;font-size:4px;color:var(--grey)">The personal attention of a specialist agent, supported by the strength of a globally recognised property network.</div>
  <div style="left:15px;top:95px;width:69px;height:22px;background:#f3f1ec;border-left:.8px solid var(--gold)"></div>
  <div style="left:96px;top:95px;width:69px;height:22px;background:#f3f1ec;border-left:.8px solid var(--teal)"></div>
  <div style="left:15px;top:126px;width:69px;height:22px;background:#f3f1ec;border-left:.8px solid var(--gold)"></div>
  <div style="left:96px;top:126px;width:69px;height:22px;background:#f3f1ec;border-left:.8px solid var(--teal)"></div>
  <div style="left:15px;top:158px;width:69px;height:22px;background:#f3f1ec;border-left:.8px solid var(--gold)"></div>
  <div style="left:96px;top:158px;width:69px;height:22px;background:#f3f1ec;border-left:.8px solid var(--teal)"></div>
  <div class="num" style="left:18px;top:103px;font-size:4.5px;color:#bbb">01</div><div class="label" style="left:35px;top:105px;font-size:1.7px">Powerful buyer database</div>
  <div class="num" style="left:99px;top:103px;font-size:4.5px;color:#bbb">02</div><div class="label" style="left:116px;top:104px;width:40px;font-size:1.7px">Luxury property marketing</div>
  <div class="num" style="left:18px;top:134px;font-size:4.5px;color:#bbb">03</div><div class="label" style="left:35px;top:136px;font-size:1.7px">Auction expertise</div>
  <div class="num" style="left:99px;top:134px;font-size:4.5px;color:#bbb">04</div><div class="label" style="left:116px;top:136px;font-size:1.7px">Digital reach</div>
  <div class="num" style="left:18px;top:166px;font-size:4.5px;color:#bbb">05</div><div class="label" style="left:35px;top:168px;font-size:1.7px">Local knowledge</div>
  <div class="num" style="left:99px;top:166px;font-size:4.5px;color:#bbb">06</div><div class="label" style="left:116px;top:168px;font-size:1.7px">National network</div>
  <div style="left:15px;top:205px;width:155px;height:31px;background:var(--night)"></div>
  <div class="brand-name" style="left:21px;top:218px;color:#fff">Keel Ashby</div>
  <div style="left:56px;top:212px;font-size:2.3px;color:#fff">Keel Ashby Coastline Group</div>
  <div class="small" style="left:56px;top:218px;width:105px;font-size:1.8px;color:#aaa">Brand platform, market reach and local expertise – used to strengthen a highly personal campaign.</div>
  <div class="folio">13</div>
</section>

<!-- Page 14 -->
<section class="page" style="left:512px;top:879px">
  <div class="photo" role="img" aria-label="Agent seated in a bright white lounge" style="left:0;top:0;width:83px;height:266px;background:linear-gradient(90deg,#efebe5 0%,#e6e0d7 60%,#f6f4f0 100%)"></div>
  <div class="label gold" style="left:95px;top:17px;font-size:1.8px">What you can expect from me</div>
  <div class="serif" style="left:95px;top:27px;font-size:8.5px">MY PROMISE<br>TO YOU</div>
  <div class="num" style="left:95px;top:69px;font-size:4.5px;color:var(--teal)">01</div><div class="label" style="left:111px;top:68px;font-size:1.7px">Transparency</div><div class="small" style="left:111px;top:73px;width:65px;font-size:1.8px">Clear advice, honest feedback and no unnecessary promises.</div>
  <div class="num" style="left:95px;top:97px;font-size:4.5px;color:var(--teal)">02</div><div class="label" style="left:111px;top:96px;font-size:1.7px">Communication</div><div class="small" style="left:111px;top:101px;width:65px;font-size:1.8px">You will know what is happening throughout your campaign.</div>
  <div class="num" style="left:95px;top:125px;font-size:4.5px;color:var(--teal)">03</div><div class="label" style="left:111px;top:124px;font-size:1.7px">Strategy</div><div class="small" style="left:111px;top:129px;width:65px;font-size:1.8px">Every decision is made with your property, market and objectives in mind.</div>
  <div class="num" style="left:95px;top:153px;font-size:4.5px;color:var(--teal)">04</div><div class="label" style="left:111px;top:152px;font-size:1.7px">Attention to detail</div><div class="small" style="left:111px;top:157px;width:65px;font-size:1.8px">Your home deserves meticulous preparation and presentation.</div>
  <div class="num" style="left:95px;top:181px;font-size:4.5px;color:var(--teal)">05</div><div class="label" style="left:111px;top:180px;font-size:1.7px">Personal service</div><div class="small" style="left:111px;top:185px;width:65px;font-size:1.8px">You deal directly with me throughout your campaign.</div>
  <div class="num" style="left:95px;top:209px;font-size:4.5px;color:var(--teal)">06</div><div class="label" style="left:111px;top:208px;font-size:1.7px">Result focus</div><div class="small" style="left:111px;top:213px;width:65px;font-size:1.8px">My role is to create the strongest possible environment for a successful sale.</div>
  <div class="folio">14</div>
</section>

<!-- Page 15 -->
<section class="page" style="left:703px;top:879px">
  <div class="photo" role="img" aria-label="Pool and river at dusk with overhanging trees" style="inset:0;background:linear-gradient(180deg,#4a4c4b 0%,#5c5648 25%,#3b4034 50%,#2c3637 75%,#3e5b62 100%)"></div>
  <div class="label" style="left:13px;top:19px;color:#bbb;font-size:1.8px">Closing</div>
  <div class="serif white" style="left:13px;top:33px;font-size:11px">YOUR HOME.<br>YOUR NEXT<br>CHAPTER.</div>
  <div class="italic" style="left:13px;top:97px;width:140px;font-size:4px;color:#ddd">Selling a home is rarely just a transaction. It is the closing of one chapter and the beginning of another.</div>
  <div class="small white" style="left:13px;top:125px;width:95px;font-size:2.2px">My role is to make the journey feel considered, strategic and personal – while creating the strongest possible opportunity for your property in the marketplace.<br><br>Thank you for considering me to represent your home. I would be honoured to tell its story.</div>
  <div style="left:13px;top:195px;width:162px;height:45px;background:rgba(30,33,34,.92)"></div>
  <div class="serif white" style="left:20px;top:205px;font-size:5.5px">MAREN TOLLIVER</div>
  <div class="label" style="left:20px;top:214px;color:#aaa;font-size:1.7px">Luxury wellness property</div>
  <div style="left:118px;top:204px;width:50px;text-align:right;font-size:2.6px;color:#fff">0471 536 802</div>
  <div style="left:98px;top:209px;width:70px;text-align:right;font-size:1.7px;color:#bbb">Hope Island • Sanctuary Cove • Helensvale</div>
  <div class="brand-name" style="left:118px;top:228px;width:50px;text-align:right;color:#fff;font-size:3px">Keel Ashby</div>
  <div class="folio" style="color:#ccc">15</div>
</section>

</body>
</html>
```